Website for a company focused on genealogical products and historical items

I need a website designed using our current branding.

Company name: R. T. Guildhouse: Keepers of Rare Lineage Prints

Our company sells ancestral art, downloadable worksheets pertaining to genealogy, and we offer weekend workshops and seminars.

the website should have the following pages:
landing page
products page: to include three different products: 1. a physical product with an intake form the customer completes online, 2. a downloadable product, and 3. a lecture/presentation booking page
about us page/history
contact page/sign up page

The website will include portraits of historical figures in gold frames, lots of white background, very clean design. We would like the website to feel fresh and clean, bright.

Target Market(s)

Older Americans interested in their family heritage and lineage

Industry/Entity Type

Genealogy, research, history, lectures

Coding

Coded - Design and coding required

Number of Pages Required

5+ page

Font styles to use
Serif
Other font styles liked:
• Libre Baskerville, Aliey, one historical script - P22 Royalist

Colors
0094D4
00A9DD
6FCCEA
C7EBF8
E9F6FB

Requirements
Must have
• must have our color branding and logo (pdf attached, and I can send original files), simple design, not too many images on each page (maybe one image per page)
Nice to have
• Nice to have clean design, all pages the same "look"
Should not have
• no black backgrounds, nothing too busy

```html
<!DOCTYPE html>
<html lang="en">
<head>
<meta charset="utf-8">
<title>R. T. Guildhouse</title>
<link href="https://fonts.googleapis.com/css2?family=Fraunces:opsz,wght@9..144,600&family=Libre+Baskerville:wght@400;700&family=Montserrat:wght@400;500&family=Pinyon+Script&display=swap" rel="stylesheet">
<style>
:root{
  --brand:#0094d4;
  --brand-bright:#00a9dd;
  --sky:#6fccea;
  --mist:#c7ebf8;
  --haze:#e9f6fb;
  --paper:#f8fcfe;
  --deep:#0a5b82;
  --ink:#0d3d56;
  --muted:#3f6478;
  --line:#8fc9e0;
  --white:#ffffff;
}
*{box-sizing:border-box;margin:0;padding:0}
html,body{width:1200px;height:3202px;overflow:hidden}
body{position:relative;background:var(--paper);font-family:"Montserrat",sans-serif;color:var(--ink)}
.abs{position:absolute}
.serif-caps{font-family:"Libre Baskerville",serif;text-transform:uppercase;letter-spacing:.02em}
.script{font-family:"Pinyon Script",cursive;color:var(--brand)}
.display{font-family:"Fraunces",serif;font-weight:600;color:var(--deep);letter-spacing:-.01em}

/* header */
.hero{position:absolute;left:0;top:0;width:1200px;height:750px;background:var(--haze);overflow:hidden}
.brand{left:96px;top:34px;display:flex;align-items:center;gap:10px;font-family:"Libre Baskerville",serif;font-weight:700;font-size:18px;color:var(--deep)}
.brand-dot{width:16px;height:16px;border-radius:50%;background:var(--brand)}
.nav a{position:absolute;top:47px;font-size:12px;color:var(--ink);text-decoration:none}
.btn-outline{left:851px;top:36px;width:123px;height:35px;border:1.5px solid var(--line);font-size:11px;display:flex;align-items:center;justify-content:space-between;padding:0 18px 0 20px;color:var(--ink)}
.btn-solid{left:982px;top:36px;width:122px;height:35px;background:var(--brand);color:var(--white);font-size:11px;display:flex;align-items:center;justify-content:center}
.hero-welcome{left:91px;top:206px;font-size:32px}
.hero-title{left:91px;top:252px;font-size:57px;line-height:63px;width:560px}
.hero-lead{left:92px;top:455px;font-size:15.5px;line-height:25px;width:470px;color:var(--muted)}
.link-line{display:flex;align-items:center;gap:18px;font-size:12.5px;color:var(--ink);white-space:nowrap}
.link-line i{display:block;width:56px;height:1px;background:var(--ink)}
.hero-image{left:722px;top:136px;width:386px;height:523px;background:radial-gradient(circle at 62% 30%,#d9d2bd 0 9%,#8a5a38 25%,#3d2f1c 55%,#2a2414 100%)}
.prompt-card{border-radius:22px;padding:22px 31px;color:var(--ink)}
.hero-prompt{left:522px;top:101px;width:370px;height:119px;background:linear-gradient(100deg,#ffffff 35%,var(--mist) 72%,var(--sky) 100%)}
.prompt-card .label{font-family:"Libre Baskerville",serif;font-size:13px;text-transform:uppercase;margin-bottom:14px}
.prompt-card p{font-size:15px;line-height:21px}

/* about */
.about-image{left:0;top:750px;width:606px;height:594px;background:linear-gradient(135deg,#b9782e 0%,#7a6a3e 25%,#b2432a 45%,#6b5a6e 65%,#c8902e 85%,#5f6a3c 100%)}
.about-prompt{left:29px;top:868px;width:315px;height:108px;background:linear-gradient(100deg,rgba(0,148,212,.85),rgba(0,169,221,.8) 70%,rgba(111,204,234,.75));color:var(--white)}
.about-prompt .label{margin-bottom:8px}
.about-style{left:553px;top:1030px;width:132px;height:107px;background:linear-gradient(100deg,rgba(0,148,212,.9),var(--sky) 60%,var(--mist));color:var(--white);padding:30px 28px}
.about-style .label{font-size:13px;margin-bottom:6px}
.about-intro{right:96px;top:846px;font-size:28px}
.about-title{right:96px;top:890px;font-size:47px;line-height:51px;text-align:right}
.about-rule{left:1096px;top:1005px;width:1px;height:56px;background:var(--ink)}
.about-text{left:706px;top:1080px;width:398px;text-align:right;font-size:14.3px;line-height:18.7px;color:var(--muted)}
.about-more{right:94px;top:1248px}

/* products */
.products-kicker{left:0;width:1200px;top:1428px;text-align:center;font-size:28px}
.products-title{left:0;width:1200px;top:1466px;text-align:center;font-size:47px}
.card{top:1569px;height:394px;width:318px;border:1.3px solid var(--line);border-radius:12px;padding:30px 28px;background:var(--white)}
.card.dark{background:var(--brand);border-color:var(--brand);color:var(--white)}
.card svg{display:block;margin-left:2px}
.card h3{font-family:"Fraunces",serif;font-weight:600;font-size:29px;line-height:34px;color:var(--deep);margin-top:46px;margin-bottom:18px}
.card.dark h3{color:var(--white)}
.card p{font-size:14px;line-height:18.7px;color:var(--muted);height:72px}
.card.dark p{color:#eef9fd}
.card .link-line{margin-top:22px;font-size:11px;font-weight:700;gap:12px;letter-spacing:0}
.card .link-line i{width:26px}
.card.dark .link-line{color:var(--white)}
.card.dark .link-line i{background:var(--white)}

/* contact */
.contact{left:78px;top:2062px;width:1044px;height:534px;background:var(--white);border-radius:14px;overflow:hidden;box-shadow:0 28px 50px rgba(0,148,212,.16)}
.contact-kicker{left:53px;top:42px;font-size:28px}
.contact-title{left:52px;top:84px;font-size:47px}
.field{border:1px solid var(--mist);font-size:9.5px;color:#6d8a99;padding:17px 17px}
.contact-image{left:528px;top:0;width:516px;height:534px;background:radial-gradient(circle at 55% 32%,#d9d2bd 0 10%,#8a5a38 28%,#3d2f1c 58%,#2a2414 100%)}
.contact-submit{left:54px;top:467px;font-size:12px;font-weight:700}
.contact-submit i{width:26px}

/* footer */
.footer{left:0;top:2763px;width:1200px;height:439px;background:var(--brand);color:var(--white)}
.footer-brand{left:168px;top:88px;width:110px;text-align:center;font-family:"Libre Baskerville",serif;font-weight:700;font-size:17px;line-height:22px}
.footer-brand .brand-dot{background:var(--white);margin:0 auto 10px;width:22px;height:22px}
.footer-col h4{font-family:"Libre Baskerville",serif;font-weight:400;font-size:12px;text-transform:uppercase;margin-bottom:26px}
.footer-col a{display:block;color:var(--white);text-decoration:none;font-size:9.5px;margin-bottom:20px}
.footer-col p{font-size:9.5px;line-height:14px;width:170px}
.news-field{margin-top:22px;width:168px;border-bottom:1px solid rgba(255,255,255,.5);display:flex;justify-content:space-between;align-items:center;padding:0 4px 7px;font-size:7.5px;color:rgba(255,255,255,.7)}
.footer-rule{left:100px;top:346px;width:987px;height:1px;background:rgba(255,255,255,.3)}
.copyright{left:0;width:1200px;top:384px;text-align:center;font-size:11px}
</style>
</head>
<body>

<header class="hero">
  <svg class="abs" style="left:0;top:0" width="1200" height="750" aria-hidden="true">
    <path d="M472 0 C470 120 560 270 700 300 C800 320 760 230 720 235" fill="none" stroke="#6fccea" stroke-width="1.6"/>
    <path d="M1108 360 C1150 400 1200 420 1205 520" fill="none" stroke="#6fccea" stroke-width="1.4"/>
    <path d="M1108 500 C1150 510 1200 500 1200 555" fill="none" stroke="#c7ebf8" stroke-width="1.2"/>
    <path d="M1108 560 C1140 575 1180 560 1190 540" fill="none" stroke="#6fccea" stroke-width="1.4"/>
  </svg>
  <div class="abs brand"><span class="brand-dot"></span>R. T. Guildhouse</div>
  <nav class="nav serif-caps">
    <a style="left:451px">Home</a>
    <a style="left:527px">Products</a>
    <a style="left:625px">About Us</a>
    <a style="left:722px">Contact</a>
  </nav>
  <svg class="abs" style="left:808px;top:45px" width="16" height="16" viewBox="0 0 16 16" aria-label="Cart">
    <path d="M1 2h2.5l2 8h7l1.5-6H4.5" fill="none" stroke="#0d3d56" stroke-width="1.2"/>
    <circle cx="6.5" cy="13" r="1.1" fill="#0d3d56"/><circle cx="12" cy="13" r="1.1" fill="#0d3d56"/>
  </svg>
  <div class="abs btn-outline serif-caps">Sign In
    <svg width="14" height="14" viewBox="0 0 14 14" aria-hidden="true"><circle cx="7" cy="7" r="6" fill="none" stroke="#0d3d56"/><circle cx="7" cy="5.5" r="2" fill="none" stroke="#0d3d56"/><path d="M3.5 11c1-2 6-2 7 0" fill="none" stroke="#0d3d56"/></svg>
  </div>
  <div class="abs btn-solid serif-caps">Get Started</div>

  <div class="abs script hero-welcome">Welcome to R. T.</div>
  <h1 class="abs display hero-title">Discover Your Heritage with R. T. Guildhouse</h1>
  <p class="abs hero-lead">Keepers of Rare Lineage Prints, Genealogy Resources, and Educational Workshops.</p>
  <div class="abs link-line serif-caps" style="left:91px;top:565px">Explore Our Collection <i></i></div>

  <div class="abs hero-image" role="img" aria-label="Portrait of a woman in a powdered curled wig and brocade gown holding an ornate frame"></div>
  <div class="abs prompt-card hero-prompt">
    <div class="label">Prompt</div>
    <p>Lady Veranne during the Roman era in the dress of a queen</p>
  </div>
</header>

<section>
  <div class="abs about-image" role="img" aria-label="Colourful cubist-style painting of musicians among tropical leaves"></div>
  <div class="abs prompt-card about-prompt">
    <div class="label">Prompt</div>
    <p>Orsel Varnhaus painting in the future</p>
  </div>
  <div class="abs prompt-card about-style">
    <div class="label">Style</div>
    <p>Artistic</p>
  </div>
  <div class="abs script about-intro">Introduction</div>
  <h2 class="abs display about-title">About Us R. T.<br>Guildhouse</h2>
  <div class="abs about-rule"></div>
  <p class="abs about-text">R. T. Guildhouse was founded with the mission to preserve and celebrate the legacies of our ancestors. Our journey began with a passion for history and a dedication to quality craftsmanship. We aim to provide individuals and families with the tools to connect with their heritage through art, education, and community.</p>
  <div class="abs link-line serif-caps about-more"><i></i> Read More</div>
</section>

<section>
  <div class="abs script products-kicker">Our Products</div>
  <h2 class="abs display products-title">Featured Products</h2>

  <article class="abs card" style="left:95px">
    <svg width="84" height="80" viewBox="0 0 84 80" aria-hidden="true" fill="none" stroke="#0a5b82" stroke-width="1.6">
      <rect x="4" y="24" width="38" height="48" transform="rotate(-12 23 48)"/>
      <circle cx="22" cy="44" r="7"/><path d="M10 66c3-10 22-12 26-2"/>
      <rect x="44" y="2" width="36" height="44" stroke="#6fccea"/>
      <circle cx="62" cy="18" r="6" stroke="#6fccea"/><path d="M52 40c2-9 18-9 20 0" stroke="#6fccea"/>
      <path d="M14 8v10M9 13h10" stroke="#6fccea"/><circle cx="72" cy="56" r="3" stroke="#6fccea"/>
    </svg>
    <h3>Custom Ancestral Portraits</h3>
    <p>Commission a beautifully crafted ancestral portrait, framed in gold and personalized to capture your family's legacy.</p>
    <div class="link-line serif-caps"><i></i> Order Your Custom Portrait</div>
  </article>

  <article class="abs card" style="left:441px">
    <svg width="84" height="80" viewBox="0 0 84 80" aria-hidden="true" fill="none" stroke="#0a5b82" stroke-width="1.6">
      <path d="M40 10h24l12 12v50H40z"/><path d="M64 10v12h12"/>
      <rect x="4" y="40" width="46" height="32" stroke="#6fccea"/>
      <circle cx="27" cy="56" r="9" stroke="#6fccea"/><path d="M10 40v-5h10v5" stroke="#6fccea"/>
      <path d="M64 34l4-4 4 4v30l-4 6-4-6z"/>
      <path d="M16 8v8M12 12h8" stroke="#6fccea"/><circle cx="26" cy="26" r="2" stroke="#6fccea"/>
    </svg>
    <h3>Genealogy Worksheets</h3>
    <p>"Download comprehensive work-sheets to trace and document your family's genealogy.</p>
    <div class="link-line serif-caps"><i></i> Start Your Journey</div>
  </article>

  <article class="abs card dark" style="left:786px">
    <svg width="84" height="80" viewBox="0 0 84 80" aria-hidden="true" fill="none" stroke="#e9f6fb" stroke-width="1.6">
      <rect x="6" y="14" width="70" height="52"/><path d="M6 58h70M2 72h78"/>
      <circle cx="52" cy="32" r="6"/><path d="M40 56c2-10 22-10 24 0"/>
      <path d="M14 26h4M22 26h10M14 36h4M22 36h10M14 46h4M22 46h10"/>
      <path d="M26 2v8M22 6h8"/>
    </svg>
    <h3>Workshops and Seminars</h3>
    <p>Book a session with our experts to delve deep into genealogical research and ancestral art.</p>
    <div class="link-line serif-caps"><i></i> Book a Workshop</div>
  </article>
</section>

<section class="abs contact">
  <div class="abs script contact-kicker">Contact Us</div>
  <h2 class="abs display contact-title">Get In Touch!</h2>
  <div class="abs field" style="left:53px;top:164px;width:199px;height:41px">First Name*</div>
  <div class="abs field" style="left:266px;top:164px;width:198px;height:41px">Last Name*</div>
  <div class="abs field" style="left:53px;top:221px;width:199px;height:41px">Email Address*</div>
  <div class="abs field" style="left:266px;top:221px;width:198px;height:41px">Phone Number*</div>
  <div class="abs field" style="left:53px;top:277px;width:411px;height:153px">Message*</div>
  <div class="abs link-line serif-caps contact-submit"><i></i> Submit Request</div>
  <div class="abs contact-image" role="img" aria-label="Portrait of a woman in a powdered curled wig and brocade gown stepping through an ornate frame"></div>
</section>

<footer class="abs footer">
  <div class="abs footer-brand"><span class="brand-dot" style="display:block"></span>R. T.<br>Guildhouse</div>
  <div class="abs footer-col" style="left:385px;top:100px">
    <h4>Navigation</h4>
    <a>Home</a><a>Products</a><a>About Us</a><a>Contact</a>
  </div>
  <div class="abs footer-col" style="left:563px;top:100px">
    <h4>Legal</h4>
    <a>Privacy Policy</a><a>Cookie Policy</a>
  </div>
  <div class="abs footer-col" style="left:735px;top:100px">
    <h4>Social</h4>
    <a>Picturefeed</a><a>Friendwall</a><a>Chirpline</a>
  </div>
  <div class="abs footer-col" style="left:870px;top:100px">
    <h4>Newsletter</h4>
    <p>Stay updated with our latest products, workshops, and special offers.</p>
    <div class="news-field">Email Address*
      <svg width="12" height="12" viewBox="0 0 12 12" aria-label="Send"><path d="M1 6l10-5-4 10-1.5-4z" fill="#ffffff"/></svg>
    </div>
  </div>
  <div class="abs footer-rule"></div>
  <p class="abs copyright">Copyright © 2024 R. T. Guildhouse. All Rights Reserved.</p>
</footer>

</body>
</html>
```